Website To Serve As A Resource For Medical Conditions

I need a website that is attractive that will be utilized to educate patients on either hepatitis c or HIV so it should be easily readable attractive but also professional. This website is going to be furnished with various topics for example, HIV treatment, HIV and Nutrition, HIV and Exercise, HIV and....

This website will also be cloned and utilized similarly for Hepatitis.

Coded - Design and coding required

1 page

0094D4
00A9DD
6FCCEA
C7EBF8
E9F6FB
A7469A
B969AE
D3A5CF
EDDBEB
F8F0F9
6B429C
8869AF
B7A5CE
E3DAEB
F3F0F8

```html
<!DOCTYPE html>
<html lang="en">
<head>
<meta charset="utf-8">
<title>ClearPath – HIV Awareness</title>
<link href="https://fonts.googleapis.com/css2?family=Open+Sans:wght@400;600;700&family=Lato:wght@400;700&display=swap" rel="stylesheet">
<style>
:root{
  --blue:#0094D4;
  --blue-bright:#3B97EE;
  --cyan:#00A9DD;
  --sky:#6FCCEA;
  --ice:#E9F6FB;
  --navy:#1F2A44;
  --navy-dark:#131B2E;
  --purple:#3A2F6B;
  --ink:#1B1B1F;
  --text:#555B66;
  --muted:#8A909A;
  --grey-bg:#F4F5F8;
  --orange:#F2994A;
  --star:#F0553A;
  --white:#FFFFFF;
}
*{box-sizing:border-box;margin:0;padding:0}
html,body{width:1200px;height:4727px;overflow:hidden}
body{position:relative;background:var(--white);font-family:"Lato",sans-serif;color:var(--ink)}
.abs{position:absolute}
.heading{font-family:"Open Sans",sans-serif;font-weight:600;color:var(--ink)}
.label{position:absolute;left:0;width:1200px;text-align:center;font-size:13px;color:var(--blue);letter-spacing:.3px}
.label span{border-bottom:1px solid var(--blue);padding-bottom:3px}
.section-title{position:absolute;left:0;width:1200px;text-align:center;font-family:"Open Sans",sans-serif;font-weight:600;font-size:40px}
.photo{position:absolute}

/* header */
.topbar{left:385px;top:0;width:815px;height:30px;background:var(--navy-dark);color:var(--white);font-size:10px;font-weight:700;display:flex;align-items:center}
.topbar .item{display:flex;align-items:center;gap:8px;height:30px}
.topbar .appt{background:var(--blue-bright);padding:0 30px;margin-left:58px;width:209px}
.brand{font-family:"Lato",sans-serif;font-weight:700;color:var(--blue-bright)}
.logo{left:128px;top:30px;font-size:34px}
.nav{left:396px;top:59px;display:flex;gap:0;font-size:11px;font-weight:700;color:#333}
.nav span{margin-right:40px}
.btn-outline-orange{left:950px;top:51px;width:118px;height:32px;border:1.5px solid var(--orange);border-radius:4px;color:var(--orange);font-size:10px;font-weight:700;display:flex;align-items:center;justify-content:center}

/* hero */
.hero{left:0;top:99px;width:1200px;height:617px;background:linear-gradient(100deg,#5d6f7c 0%,#8e9ea8 45%,#6e8593 70%,#4b5d6b 100%)}
.hero-badge{left:516px;top:299px;width:164px;height:34px;background:var(--blue-bright);color:var(--white);font-size:10px;font-weight:700;display:flex;align-items:center;justify-content:center}
.hero-title{left:0;top:350px;width:1200px;text-align:center;color:var(--white);font-family:"Open Sans",sans-serif;font-weight:700;font-size:58px;line-height:70px;letter-spacing:1.5px}
.hero-btn{left:516px;top:517px;width:166px;height:44px;border:1.5px solid var(--white);color:var(--white);font-size:11px;font-weight:700;display:flex;align-items:center;justify-content:center}

/* about */
.about-img-a{left:79px;top:846px;width:246px;height:365px;background:linear-gradient(160deg,#7b8fa0,#c9d2da 60%,#6d5a58)}
.about-img-b{left:339px;top:800px;width:226px;height:222px;background:linear-gradient(150deg,#cfd8dc,#eef1f3 50%,#8e9aa6)}
.about-img-c{left:339px;top:1033px;width:226px;height:224px;background:linear-gradient(150deg,#8aa0ae,#d9dfe3 50%,#5d7283)}
.about-badge{left:290px;top:985px;width:92px;height:92px;border-radius:50%;background:var(--white);box-shadow:0 4px 14px rgba(0,0,0,.12);display:flex;align-items:center;justify-content:center}
.about-text{left:606px;top:818px;width:540px}
.about-text .eyebrow{font-size:13px;color:var(--blue);border-bottom:1px solid var(--blue);display:inline-block;padding-bottom:3px}
.about-text h2{font-size:42px;line-height:51px;margin-top:20px}
.about-text h3{font-family:"Open Sans",sans-serif;font-weight:600;font-size:20px;margin-top:22px}
.about-text p{font-size:13px;line-height:21px;color:var(--text);margin-top:14px}
.about-text p+p{margin-top:10px}
.btn-solid{left:604px;top:1187px;width:154px;height:44px;background:var(--cyan);color:var(--white);font-size:15px;font-weight:700;display:flex;align-items:center;justify-content:center;gap:14px;border-radius:2px}

/* info */
.info-bg{left:0;top:1321px;width:1200px;height:652px;background:var(--grey-bg)}
.topic-img{top:1596px;width:325px;height:261px}
.topic-icon{width:106px;height:106px;border-radius:50%;border:1.5px solid var(--blue-bright);display:flex;align-items:center;justify-content:center;top:1543px}
.topic-icon span{width:86px;height:86px;border-radius:50%;background:var(--blue-bright);display:flex;align-items:center;justify-content:center}
.topic-card{top:1813px;width:273px;height:95px;background:var(--white);box-shadow:0 6px 14px rgba(0,0,0,.08);text-align:center;padding-top:22px}
.topic-card b{display:block;font-family:"Open Sans",sans-serif;font-weight:600;font-size:19px;color:var(--blue-bright)}
.topic-card span{font-size:18px;color:#333}

/* call band */
.call{left:0;top:1973px;width:1200px;height:256px;background:linear-gradient(90deg,#27406d,#2e4a7a 50%,#22365d)}
.call-text{left:0;top:2058px;width:1200px;text-align:center;color:var(--white);font-family:"Open Sans",sans-serif;font-size:32px;line-height:39px}
.call-text em{font-style:normal;color:var(--blue-bright)}
.call-pill{left:350px;top:2198px;width:500px;height:55px;background:var(--white);border-radius:4px;box-shadow:0 6px 16px rgba(0,0,0,.12);display:flex;align-items:center;justify-content:space-around;font-size:17px;color:#222;padding:0 10px}

/* why */
.why-photo{left:807px;top:2395px;width:393px;height:673px;background:linear-gradient(170deg,#e8eef3 0%,#b9c7d3 40%,#6c8db5 80%,#3d63a0 100%)}
.why-card{width:233px;height:261px;background:var(--white);box-shadow:0 4px 14px rgba(0,0,0,.08);text-align:center;padding-top:30px}
.why-card .ic{width:84px;height:84px;border-radius:50%;background:#EEF0F3;margin:0 auto;display:flex;align-items:center;justify-content:center}
.why-card h4{font-family:"Open Sans",sans-serif;font-weight:600;font-size:17px;margin-top:28px;color:#222}
.why-card p{font-size:14px;line-height:23px;color:#333;margin:6px auto 0;width:190px}
.why-card.active{background:var(--cyan)}
.why-card.active .ic{background:var(--white)}
.why-card.active h4,.why-card.active p{color:var(--white)}

/* testimonials */
.testi-band{left:0;top:3068px;width:1200px;height:360px;background:linear-gradient(90deg,#2e2860,#3a336f 50%,#2b2559)}
.testi-card{top:3308px;width:299px;height:325px;background:var(--white);box-shadow:0 6px 18px rgba(0,0,0,.1);padding:42px 40px 0 40px}
.stars{color:var(--star);font-size:19px;letter-spacing:3px}
.testi-card p{font-size:14px;line-height:25px;color:var(--text);margin-top:12px}
.testi-card hr{border:0;border-top:1.5px solid #ddd;margin-top:28px;width:220px}
.person{display:flex;align-items:center;gap:14px;margin-top:22px}
.avatar{width:58px;height:58px;border-radius:50%;background:linear-gradient(135deg,#9aa7b4,#5a6978)}
.person b{font-family:"Open Sans",sans-serif;font-weight:600;font-size:16px;color:#333;display:block}
.person span{font-size:13px;color:var(--muted)}
.quote{width:46px;height:46px;border-radius:50%;background:var(--blue-bright);display:flex;align-items:center;justify-content:center;top:3346px}

/* contact + footer */
.footer{left:0;top:4220px;width:1200px;height:450px;background:linear-gradient(180deg,#1b1b1f,#26272b)}
.contact-card{left:139px;top:3868px;width:920px;height:457px;background:var(--white);border-radius:10px;box-shadow:0 8px 24px rgba(0,0,0,.12);overflow:hidden}
.contact-photo{left:0;top:0;width:478px;height:457px;background:linear-gradient(120deg,#d9dde0,#f2ede6 45%,#2c3a5a 80%)}
.form{left:510px;top:40px;width:380px}
.form .brand{font-size:36px}
.form h3{font-family:"Open Sans",sans-serif;font-weight:400;font-size:29px;color:#222;margin-top:22px}
.field{border:1px solid #ccc;border-radius:3px;font-size:11px;color:#888;padding:0 8px;height:37px;display:flex;align-items:center}
.btn-send{background:var(--blue-bright);color:var(--white);font-size:12px;font-weight:700;height:37px;border-radius:3px;display:flex;align-items:center;justify-content:center}
.foot-logo{left:0;top:4344px;width:1200px;text-align:center;color:var(--white);font-size:72px;font-family:"Lato",sans-serif;font-weight:700;letter-spacing:2px}
.foot-nav{left:0;top:4490px;width:1200px;display:flex;justify-content:center;gap:50px;color:var(--white);font-size:14px}
.foot-rule{left:139px;top:4543px;width:920px;height:1px;background:#55565c}
.foot-item{top:4585px;display:flex;align-items:center;gap:14px;color:var(--white);font-size:13px;line-height:18px}
.foot-item .ring{width:56px;height:56px;border-radius:50%;border:1.5px solid #999;display:flex;align-items:center;justify-content:center}
.foot-sep{top:4580px;width:1px;height:64px;background:#55565c}
.bottom-bar{left:0;top:4670px;width:1200px;height:57px;background:var(--blue-bright);color:var(--white);font-size:13px}
.social{display:flex;gap:8px;position:absolute;right:135px;top:17px}
.social span{width:24px;height:24px;border:1.5px solid var(--white);border-radius:2px}
</style>
</head>
<body>

<!-- Header -->
<div class="abs topbar">
  <div class="item" style="margin-left:60px">
    <svg width="14" height="14" viewBox="0 0 24 24" fill="none" stroke="#fff" stroke-width="2"><path d="M5 3h4l2 5-3 2a12 12 0 0 0 6 6l2-3 5 2v4a2 2 0 0 1-2 2A17 17 0 0 1 3 5a2 2 0 0 1 2-2z"/></svg>
    555 - 010 - 4421
  </div>
  <div class="item appt">
    <svg width="13" height="13" viewBox="0 0 24 24" fill="none" stroke="#fff" stroke-width="2"><rect x="3" y="5" width="18" height="16" rx="2"/><path d="M3 10h18M8 3v4M16 3v4"/></svg>
    REQUEST AN APPOINTMENT
  </div>
  <div class="item" style="margin-left:45px">
    <svg width="12" height="14" viewBox="0 0 24 24" fill="none" stroke="#fff" stroke-width="2"><path d="M12 22s7-7 7-12a7 7 0 0 0-14 0c0 5 7 12 7 12z"/><circle cx="12" cy="10" r="2.5"/></svg>
    1234 Some Place Somewhere
  </div>
</div>
<div class="abs brand logo">ClearPath</div>
<nav class="abs nav"><span>Home</span><span>About Us</span><span>Services</span><span>Resources</span><span>Gallery</span><span>Doctors</span><span>Contact Us</span></nav>
<div class="abs btn-outline-orange">CONTACT US</div>

<!-- Hero -->
<div class="abs hero" role="img" aria-label="Hospital corridor with a doctor and a nurse reviewing a clipboard"></div>
<div class="abs hero-badge">WELCOME TO ClearPath</div>
<h1 class="abs hero-title">GLOBAL EXPERTISE IN<br>HIV Awareness</h1>
<div class="abs hero-btn">ABOUT COMPANY</div>

<!-- About -->
<div class="photo about-img-a" role="img" aria-label="Doctor and nurse discussing notes on a clipboard"></div>
<div class="photo about-img-b" role="img" aria-label="Doctors in conversation at a desk"></div>
<div class="photo about-img-c" role="img" aria-label="Medical team gathered around a table seen from above"></div>
<div class="abs about-badge">
  <svg width="40" height="40" viewBox="0 0 40 40" fill="none" stroke="#3B97EE" stroke-width="2"><path d="M8 32h24M12 32l6-10M16 14l8-6 4 4-8 6zM18 22a8 8 0 1 0 8-8"/></svg>
</div>
<div class="abs about-text">
  <span class="eyebrow">WHO WE ARE</span>
  <h2 class="heading">From Stigma to Solidarity:<br>HIV Education</h2>
  <h3>Knowledge Is Our Best Weapon Against HIV</h3>
  <p>Lorem ipsum dolor sit amet, consectetur adipiscing elit, sed do eiusmod temp or incididunt ut labore et dolore magna aliqua. Ut enim ad minim veniam, quis laboris nisi ut aliquip ex ea commodo consequat.</p>
  <p>Lorem ipsum dolor sit amet, consectetur adipiscing elit, sed do eiusmod temp or incididunt ut labore et dolore magna aliqua.</p>
</div>
<div class="abs btn-solid">Contact us
  <svg width="18" height="12" viewBox="0 0 18 12" fill="none" stroke="#fff" stroke-width="1.6"><path d="M1 6h15M11 1l5 5-5 5"/></svg>
</div>

<!-- Information -->
<div class="abs info-bg"></div>
<div class="label" style="top:1397px"><span>WHO WE ARE</span></div>
<h2 class="section-title" style="top:1433px">Information We Provide</h2>

<div class="photo topic-img" style="left:86px;background:linear-gradient(135deg,#8d9cab,#c7cfd6 55%,#4f6c8f)" role="img" aria-label="Doctor comforting an older patient"></div>
<div class="photo topic-img" style="left:437px;background:linear-gradient(135deg,#aab7c4,#dfe5ea 55%,#6a86a4)" role="img" aria-label="Smiling doctor in conversation"></div>
<div class="photo topic-img" style="left:787px;background:linear-gradient(135deg,#c8d2da,#eef2f5 55%,#7f98b2)" role="img" aria-label="Doctor taking notes at a desk"></div>

<div class="abs topic-icon" style="left:196px"><span><svg width="40" height="40" viewBox="0 0 40 40" fill="none" stroke="#fff" stroke-width="2"><path d="M8 32h24M12 32l6-10M16 14l8-6 4 4-8 6zM18 22a8 8 0 1 0 8-8"/></svg></span></div>
<div class="abs topic-icon" style="left:547px"><span><svg width="40" height="40" viewBox="0 0 40 40" fill="none" stroke="#fff" stroke-width="2"><circle cx="20" cy="21" r="9"/><circle cx="20" cy="9" r="3"/><circle cx="9" cy="27" r="3"/><circle cx="31" cy="27" r="3"/></svg></span></div>
<div class="abs topic-icon" style="left:897px"><span><svg width="40" height="40" viewBox="0 0 40 40" fill="none" stroke="#fff" stroke-width="2"><circle cx="20" cy="14" r="5"/><path d="M11 32c0-6 4-10 9-10s9 4 9 10z"/><circle cx="9" cy="16" r="3"/><circle cx="31" cy="16" r="3"/></svg></span></div>

<div class="abs topic-card" style="left:112px"><b>HIV treatment</b><span>HIV treatment</span></div>
<div class="abs topic-card" style="left:463px"><b>HIV and Nutrition</b><span>HIV and Nutrition</span></div>
<div class="abs topic-card" style="left:813px"><b>HIV and Exercise</b><span>HIV and Exercise</span></div>

<!-- Call band -->
<div class="abs call" role="img" aria-label="Dim background photo of a care team"></div>
<div class="abs call-text">We're On <em>Call 24/7</em> to React Promptly to Your Service<br>Needs, Don't Hesitate to Call</div>
<div class="abs call-pill"><span>+ (001) 234-567-890</span><span>[or]</span><span>info@example.com</span></div>

<!-- Why choose -->
<div class="label" style="top:2310px"><span>WHY CHOOSE US</span></div>
<h2 class="section-title" style="top:2345px">Why Choose Us</h2>
<div class="photo why-photo" role="img" aria-label="Doctor and nurse wearing masks reviewing a clipboard"></div>

<div class="abs why-card" style="left:95px;top:2472px"><div class="ic"><svg width="38" height="38" viewBox="0 0 40 40" fill="none" stroke="#555" stroke-width="1.8"><circle cx="20" cy="13" r="6"/><path d="M8 36c0-8 5-13 12-13s12 5 12 13z"/></svg></div><h4>Empathy and Support</h4><p>Everything we do revolves around our clients and their needs</p></div>
<div class="abs why-card active" style="left:352px;top:2472px"><div class="ic"><svg width="38" height="38" viewBox="0 0 40 40" fill="none" stroke="#3B97EE" stroke-width="1.8"><circle cx="20" cy="13" r="6"/><path d="M8 36c0-8 5-13 12-13s12 5 12 13z"/></svg></div><h4>Community Engagement</h4><p>Everything we do revolves around our clients and their needs</p></div>
<div class="abs why-card" style="left:609px;top:2472px"><div class="ic"><svg width="38" height="38" viewBox="0 0 40 40" fill="none" stroke="#555" stroke-width="1.8"><circle cx="20" cy="13" r="6"/><path d="M8 36c0-8 5-13 12-13s12 5 12 13z"/></svg></div><h4>Regular Updates</h4><p>Everything we do revolves around our clients and their needs</p></div>
<div class="abs why-card" style="left:95px;top:2756px"><div class="ic"><svg width="38" height="38" viewBox="0 0 40 40" fill="none" stroke="#555" stroke-width="1.8"><circle cx="20" cy="13" r="6"/><path d="M8 36c0-8 5-13 12-13s12 5 12 13z"/></svg></div><h4>Privacy and Security</h4><p>Everything we do revolves around our clients and their needs</p></div>
<div class="abs why-card" style="left:352px;top:2756px"><div class="ic"><svg width="38" height="38" viewBox="0 0 40 40" fill="none" stroke="#555" stroke-width="1.8"><circle cx="20" cy="13" r="6"/><path d="M8 36c0-8 5-13 12-13s12 5 12 13z"/></svg></div><h4>Resource Library</h4><p>Everything we do revolves around our clients and their needs</p></div>
<div class="abs why-card" style="left:609px;top:2756px"><div class="ic"><svg width="38" height="38" viewBox="0 0 40 40" fill="none" stroke="#555" stroke-width="1.8"><circle cx="20" cy="13" r="6"/><path d="M8 36c0-8 5-13 12-13s12 5 12 13z"/></svg></div><h4>Non-Discrimination</h4><p>Everything we do revolves around our clients and their needs</p></div>

<!-- Testimonials -->
<div class="abs testi-band" role="img" aria-label="Dim purple-toned photo of medical staff"></div>
<div class="label" style="top:3161px;color:var(--white)"><span style="border-color:var(--white)">WHO WE ARE</span></div>
<h2 class="section-title" style="top:3196px;color:var(--white)">What Clients Are Saying</h2>

<div class="abs testi-card" style="left:112px"><div class="stars">★★★★★</div><p>Lorem ipsum dolor sit amet, co nsectetur adipiscing elit, sed do eiusmod tempor incididunt ut labore et dolore</p><hr><div class="person"><div class="avatar" role="img" aria-label="Client portrait"></div><div><b>Mara Linden</b><span>Business Person</span></div></div></div>
<div class="abs testi-card" style="left:461px"><div class="stars">★★★★★</div><p>Lorem ipsum dolor sit amet, co nsectetur adipiscing elit, sed do eiusmod tempor incididunt ut labore et dolore</p><hr><div class="person"><div class="avatar" role="img" aria-label="Client portrait"></div><div><b>Mara Linden</b><span>Business Person</span></div></div></div>
<div class="abs testi-card" style="left:807px"><div class="stars">★★★★★</div><p>Lorem ipsum dolor sit amet, co nsectetur adipiscing elit, sed do eiusmod tempor incididunt ut labore et dolore</p><hr><div class="person"><div class="avatar" role="img" aria-label="Client portrait"></div><div><b>Mara Linden</b><span>Business Person</span></div></div></div>
<div class="abs quote" style="left:88px"><svg width="22" height="18" viewBox="0 0 22 18" fill="#fff"><path d="M0 18V9C0 4 3 1 8 0v3C5 4 4 6 4 8h5v10zM13 18V9c0-5 3-8 8-9v3c-3 1-4 3-4 5h5v10z"/></svg></div>
<div class="abs quote" style="left:437px"><svg width="22" height="18" viewBox="0 0 22 18" fill="#fff"><path d="M0 18V9C0 4 3 1 8 0v3C5 4 4 6 4 8h5v10zM13 18V9c0-5 3-8 8-9v3c-3 1-4 3-4 5h5v10z"/></svg></div>
<div class="abs quote" style="left:784px"><svg width="22" height="18" viewBox="0 0 22 18" fill="#fff"><path d="M0 18V9C0 4 3 1 8 0v3C5 4 4 6 4 8h5v10zM13 18V9c0-5 3-8 8-9v3c-3 1-4 3-4 5h5v10z"/></svg></div>

<!-- Contact -->
<div class="label" style="top:3717px"><span>CONTACT US</span></div>
<h2 class="section-title" style="top:3752px">Get in touch with us</h2>

<div class="abs footer"></div>
<svg class="abs" style="left:0;top:4160px" width="1200" height="200" viewBox="0 0 1200 200">
  <path d="M0 60 Q60 80 139 140 L139 200 L0 200Z" fill="#3B97EE"/>
  <path d="M1059 80 Q1150 110 1200 160 L1200 200 L1059 200Z" fill="#3B97EE"/>
</svg>

<div class="abs contact-card">
  <div class="abs contact-photo" role="img" aria-label="Patient listening to a clinician during a consultation"></div>
  <div class="abs form">
    <div class="brand">ClearPath</div>
    <h3>Please fill out the form</h3>
    <div class="field" style="margin-top:28px">Name</div>
    <div style="display:flex;gap:14px;margin-top:16px"><div class="field" style="flex:1">Phone</div><div class="field" style="flex:1">Email</div></div>
    <div class="field" style="margin-top:16px;height:68px;align-items:flex-start;padding-top:10px">Message</div>
    <div class="btn-send" style="margin-top:16px">Send</div>
  </div>
</div>

<!-- Footer -->
<div class="abs foot-logo">ClearPath</div>
<nav class="abs foot-nav"><span>HOME</span><span>SERVICES</span><span>ABOUT US</span><span>TESTIMONIALS</span><span>BLOG</span></nav>
<div class="abs foot-rule"></div>
<div class="abs foot-item" style="left:172px"><div class="ring"><svg width="28" height="28" viewBox="0 0 24 24" fill="none" stroke="#fff" stroke-width="1.4"><circle cx="12" cy="12" r="9"/><path d="M3 12h18M12 3c3 3 3 15 0 18M12 3c-3 3-3 15 0 18"/></svg></div><div>123, Building Name, Street<br>City, State XY 123456</div></div>
<div class="abs foot-sep" style="left:428px"></div>
<div class="abs foot-item" style="left:504px"><div class="ring"><svg width="24" height="28" viewBox="0 0 24 28" fill="none" stroke="#fff" stroke-width="1.4"><rect x="7" y="3" width="10" height="22" rx="2"/><path d="M3 10v8M21 10v8"/></svg></div><div>PHONE<br>(123) 456 7890</div></div>
<div class="abs foot-sep" style="left:748px"></div>
<div class="abs foot-item" style="left:826px"><div class="ring"><svg width="28" height="24" viewBox="0 0 28 24" fill="none" stroke="#fff" stroke-width="1.4"><path d="M3 10l11-7 11 7v12H3z"/><path d="M3 10l11 7 11-7"/></svg></div><div>EMAIL<br>info@company.com</div></div>

<div class="abs bottom-bar">
  <span style="position:absolute;left:147px;top:19px">ClearPath</span>
  <div class="social"><span></span><span></span><span></span><span></span></div>
</div>

</body>
</html>
```